Website Design Needed for Performance Horse Trading Business

We require a website designed for Saddlemire, a new business which lists top quality performance stock horse bloodlines for sale. Our Australian company caters to the Australian Stock Horse, Quarter Horse and Paint Horse breeds of horse used for performance events such as Camp drafting and Cutting. The website design needs to communicate quality, have a professional look while maintaining a western, rural feel.
Colour schemes that we are looking for are either grey and orange, navy and grey or brown and grey.
The logo for the website has been attached below
Design deliverables are as follows:
-Main Page
-Horses for Sale Page
-Horse Listing Page
-Html & CSS files for pages
MAIN PAGE
----------------
Description: This page is where customers land, search for horses, see premium horses
Elements which need to be included on the main page are
-a horse filter section, allowing customers to search for horse listings by filtering attributes.
-premium listings displaying large photos of horse, price and location.
Horses for Sale PAGE
---------------------------------
Description: This page displays a list of available horses for sale as per the filtered results.
Elements which need to be included on this page are
- a filter panel which allows customers to filter results
- list of horses available for sale
Horse Listing Page
-------------------------------
Description: This page displays all the information about the horse for sale.
Screenshots of the basic program are attached for the Horses for Sale Page and the Horse Listing Page to give an idea of the elements required ONLY and should not be thought of as a design guideline.
Webpage HEADER
-------------------------
The Header section of the website should include login/signup buttons, 'my account' buttons (or links) as well as a featured link/button that says 'Sell Your Horse'
Updates
Thank you all for your designs so far. We would like to see the Sell Your Horse section featured more in the website design to attract customers. This would be as a button or highlighted link that is eye catching in the primary section of the website design of the main page. Perhaps placing it on the right hand side adjacent to the search function lets customers make the mental decision as to whether they are looking to buy or looking to sell when they visit the website. The wording above or near the button would be 'Advertise your horse with us' with the words on the button being 'Create Ad!'.
Industry/Entity Type
Events
Look and feel
Each slider illustrates characteristics of the customer's brand and the style your logo design should communicate.

```html
<!DOCTYPE html>
<html lang="en">
<head>
<meta charset="utf-8">
<title>Saddlemire – The Best Australian Bred Horses</title>
<link href="https://fonts.googleapis.com/css2?family=Questrial&family=Arimo:wght@400;700&family=Cinzel:wght@700&display=swap" rel="stylesheet">
<style>
  :root {
    --page-bg: #f0f0f0;
    --brown-dark: #5b3b26;
    --brown-mid: #7b6356;
    --brown-text: #5a3519;
    --white: #ffffff;
    --tab-bg: #eeeeee;
    --ink: #1c1c1c;
  }
  * { box-sizing: border-box; margin: 0; padding: 0; }
  html, body { width: 1200px; height: 900px; overflow: hidden; background: var(--page-bg); }
  body { position: relative; font-family: "Arimo", Arial, sans-serif; }

  .site-header { position: absolute; left: 0; top: 0; width: 1200px; height: 120px; background: var(--page-bg); }
  .brand { position: absolute; left: 36px; top: 30px; display: flex; align-items: center; gap: 12px;
    font-family: "Cinzel", serif; font-weight: 700; font-size: 46px; color: var(--ink); letter-spacing: 1px; }
  .brand-mark { width: 14px; height: 14px; background: var(--ink); border-radius: 50%; }
  .main-nav { position: absolute; right: 27px; top: 48px; display: flex; gap: 17px; }
  .main-nav a { font-family: "Questrial", sans-serif; font-size: 20px; color: var(--brown-text); text-decoration: none; }

  .hero { position: absolute; left: 0; top: 120px; width: 1200px; height: 421px;
    background: linear-gradient(180deg, #6f8a45 0%, #5a3a22 30%, #3d2a1c 48%, #6f9a3c 70%, #8fb95a 100%); }
  .hero-title { position: absolute; left: 30px; top: 28px; font-family: "Questrial", sans-serif; font-size: 55px;
    line-height: 67px; color: var(--white); text-transform: uppercase; text-shadow: 2px 3px 4px rgba(0,0,0,.55); }

  .login-tab { position: absolute; right: 0; top: 120px; width: 352px; height: 51px; }
  .login-tab svg { position: absolute; inset: 0; }
  .login-tab label { position: absolute; left: 40px; top: 14px; font-family: "Questrial", sans-serif; font-size: 20px; color: var(--brown-text); }
  .login-tab .field { position: absolute; left: 113px; top: 9px; width: 213px; height: 27px; }

  .search-tab { position: absolute; left: 0; top: 487px; width: 350px; height: 54px; }
  .search-tab svg { position: absolute; inset: 0; }
  .search-tab label { position: absolute; left: 18px; top: 18px; font-family: "Questrial", sans-serif; font-size: 20px; color: var(--brown-text); }
  .search-tab .field { position: absolute; left: 101px; top: 17px; width: 210px; height: 26px; }

  .field { border: 2px solid var(--brown-dark); border-radius: 14px; background: var(--white); }

  .premium-card { position: absolute; top: 553px; width: 233px; height: 302px; }
  .premium-card.tone-light { --card: var(--brown-mid); }
  .premium-card.tone-dark { --card: var(--brown-dark); }
  .card-title { height: 25px; background: var(--card); color: var(--white); font-family: "Questrial", sans-serif;
    font-size: 16px; text-align: center; line-height: 26px; }
  .card-photo { height: 174px; }
  .card-info { height: 103px; background: var(--card); color: var(--white); font-size: 16px; text-align: center; padding-top: 41px; line-height: 20px; }

  .sell-panel { position: absolute; left: 831px; top: 615px; width: 331px; }
  .sell-button { height: 68px; background: var(--brown-dark); border-radius: 8px 8px 0 0; color: var(--white);
    font-family: "Arimo", sans-serif; font-size: 30px; text-align: center; line-height: 70px; }
  .sell-photo { height: 172px; background: linear-gradient(180deg, #3c87c6 0%, #9cc6e6 35%, #8fbc3d 60%, #5f9a24 100%); }

  .site-footer { position: absolute; left: 0; top: 866px; width: 1200px; height: 34px; background: var(--brown-dark);
    display: flex; justify-content: center; align-items: center; gap: 12px; }
  .site-footer a { font-family: "Questrial", sans-serif; font-size: 15px; color: var(--white); text-decoration: none; }
</style>
</head>
<body>
  <header class="site-header">
    <div class="brand"><span class="brand-mark"></span>Saddlemire</div>
    <nav class="main-nav">
      <a href="#">HOME</a><a href="#">SALES</a><a href="#">BREEDS</a><a href="#">ABOUT US</a>
    </nav>
  </header>

  <section class="hero" role="img" aria-label="Photo of several bay horses grazing in a green paddock">
    <h1 class="hero-title">The<br>Best<br>Australian<br>Bred<br>Horses</h1>
  </section>

  <div class="login-tab">
    <svg width="352" height="51" viewBox="0 0 352 51"><polygon points="0,0 352,0 352,51 40,51" fill="var(--tab-bg)"/></svg>
    <label>LOGIN:</label>
    <div class="field"></div>
  </div>

  <div class="search-tab">
    <svg width="350" height="54" viewBox="0 0 350 54"><polygon points="0,0 305,0 350,54 0,54" fill="var(--tab-bg)"/></svg>
    <label>SEARCH</label>
    <div class="field"></div>
  </div>

  <article class="premium-card tone-light" style="left:19px">
    <div class="card-title">Australian Stock Horse</div>
    <div class="card-photo" role="img" aria-label="Photo of a white horse galloping along a beach" style="background:linear-gradient(180deg,#8fb0d6 0%,#c9d6e0 45%,#9fb2b8 65%,#c7b49a 100%)"></div>
    <div class="card-info">Location: Granville, QLD<br>Price: $5,000.00</div>
  </article>

  <article class="premium-card tone-dark" style="left:267px">
    <div class="card-title">Brood Mare Quarter Horse</div>
    <div class="card-photo" role="img" aria-label="Photo of a chestnut quarter horse mare standing in a yard" style="background:linear-gradient(180deg,#e2e6ea 0%,#6c8f4c 35%,#a0522d 60%,#b89a78 80%,#6d9a45 100%)"></div>
    <div class="card-info">Location: Granville, QLD<br>Price: $10,500.00</div>
  </article>

  <article class="premium-card tone-light" style="left:520px">
    <div class="card-title">Australian Stock Horse</div>
    <div class="card-photo" role="img" aria-label="Photo of a chestnut and white paint horse head" style="background:linear-gradient(90deg,#5f7a3a 0%,#8a4a2a 35%,#f2efe8 70%,#7c9a4a 100%)"></div>
    <div class="card-info">Location: Granville, QLD<br>Price: $2,300.00</div>
  </article>

  <aside class="sell-panel">
    <div class="sell-button">&lt;&lt;Sell Your Horse&gt;&gt;</div>
    <div class="sell-photo" role="img" aria-label="Photo of a paint horse grazing in a green field under a blue sky"></div>
  </aside>

  <footer class="site-footer">
    <a href="#">HOME</a><a href="#">SALES</a><a href="#">BREEDS</a><a href="#">ABOUT US</a>
  </footer>
</body>
</html>
```